Restaurant business revamping our look and need a new modern menu

We need a new menu that is appealing, similar to the look of our new logo while also keeping our "cozy, clean, Midland staple" feel and gets peoples eyes on the high price items and top sellers. We are a deli that's been around since 1984, with lots of Burgers, Curly Fries, Reuben, Salads, etc.
Once we like that menu, we will need our pizza specials menu updated to look similar.

Please refer to our website for menu word format www.tolbertsofcrestvale.com

Target Market(s)

Every day Midlanders

Industry/Entity Type

Restaurant

Requirements
Must have
• Current menu is a trifold - not a must have but nice layout

```html
<!DOCTYPE html>
<html lang="en">
<head>
<meta charset="utf-8">
<title>Tolbert's Deli Menu</title>
<link rel="stylesheet" href="https://fonts.googleapis.com/css2?family=Oswald:wght@400;500;600&family=Crimson+Pro:ital,wght@0,400;0,600;0,700;1,400;1,600;1,700&display=swap">
<style>
:root{
  --paper:#fbf8ef;
  --ink:#161616;
  --red:#d9493a;
  --red-dark:#a8322a;
  --backdrop:#e7e4dd;
  --soft:#3a3a3a;
}
*{margin:0;padding:0;box-sizing:border-box}
html,body{width:1200px;height:1200px;overflow:hidden;background:var(--backdrop)}
.menu{position:absolute;left:227px;top:15px;width:1098px;height:1720px;background:var(--paper);transform:scale(0.68);transform-origin:0 0;color:var(--ink);font-family:"Crimson Pro",serif}
.abs{position:absolute}
/* header */
.brand{left:30px;top:20px;width:180px;height:180px;display:flex;flex-direction:column;align-items:center;justify-content:center;gap:10px}
.brand-dot{width:22px;height:22px;border-radius:50%;background:var(--red)}
.brand-name{font-family:"Oswald",sans-serif;font-weight:600;font-size:40px;color:var(--ink);letter-spacing:1px}
.intro{left:237px;top:36px;width:840px;font-style:italic;font-size:17.5px;line-height:23px}
.intro b{font-weight:700}
.contact{left:237px;top:154px;width:840px;display:flex;justify-content:space-between;font-weight:700;font-size:18px}
.contact span{display:flex;align-items:center;gap:7px}
.contact svg{width:13px;height:13px}
.rule{left:0;top:209px;width:1098px;height:2px;background:var(--red)}
/* columns */
h2.sec{font-family:"Oswald",sans-serif;font-weight:600;text-transform:uppercase;line-height:1}
.item{margin-bottom:9px}
.row{display:flex;justify-content:space-between;align-items:baseline}
.row h4{font-family:"Oswald",sans-serif;font-weight:400;font-size:17px;text-transform:uppercase;line-height:1.25}
.price{color:var(--red);font-size:12.5px;white-space:nowrap;padding-left:8px}
.item p,.note{font-style:italic;font-size:11.5px;line-height:14px;padding-right:12px}
.add{display:flex;justify-content:space-between;font-style:italic;font-size:11.5px;line-height:18px}
.add .price{font-style:normal}
.red{color:var(--red)}
.art{background:linear-gradient(135deg,#d9d4c7,#b9b2a3);border-radius:6px}
/* soup & salad */
.soup-head{left:24px;top:245px;font-size:52px}
.soup-head .amp{color:var(--red)}
.soup-art{left:190px;top:240px;width:110px;height:100px}
.soup-list{left:24px;top:368px;width:322px}
.soup-list .soup{font-family:"Oswald",sans-serif;font-size:16px;text-transform:uppercase;line-height:29px}
.soup-list .soup .price{font-family:"Crimson Pro",serif;font-size:13px}
.salads{left:24px;top:522px;width:322px}
/* cold */
.cold-band{left:24px;top:1248px;width:316px;height:56px;background:var(--red);color:var(--paper);font-size:38px;display:flex;align-items:center;justify-content:center}
.cold{left:24px;top:1317px;width:322px}
.cold .sides{font-size:11.5px;margin-bottom:10px}
.cold .extras{font-size:11.5px;font-weight:700;font-style:italic;line-height:13.5px;margin-bottom:12px;text-transform:uppercase}
/* hot sandwiches */
.hot-head{left:545px;top:232px;width:375px;text-align:center}
.hot-head h2{font-size:50px;padding:10px 0}
.hot-head .bar{height:2px;background:var(--ink);position:relative}
.hot-head .bar::after{content:"";position:absolute;left:50%;top:-5px;width:10px;height:10px;background:var(--red);transform:translateX(-50%) rotate(45deg)}
.hot-a{left:395px;top:330px;width:320px}
.hot-b{left:752px;top:330px;width:320px}
.hot-a .item,.hot-b .item{margin-bottom:8px}
/* burgers */
.burger-band{left:410px;top:748px}
.burger-art{left:510px;top:764px;width:54px;height:52px}
.dog-art{left:892px;top:772px;width:70px;height:36px}
.burger-title{left:410px;top:770px;width:642px;text-align:center;color:var(--paper);font-size:38px}
.burger-opts{left:395px;top:850px;width:400px;font-style:italic;font-size:11.5px}
.burger-a{left:395px;top:872px;width:320px}
.burger-a .item{margin-bottom:6px}
.burger-b{left:752px;top:875px;width:320px}
/* appetizers */
.app-head{left:395px;top:1168px;width:245px;display:flex;align-items:center;gap:8px}
.app-head h2{font-size:40px}
.app-head svg{width:22px;height:20px}
.app{left:395px;top:1220px;width:320px}
/* kids */
.kids-band{left:755px;top:1100px}
.kids-title{left:784px;top:1107px;width:256px;text-align:center;color:var(--paper);font-size:38px}
.kids{left:752px;top:1210px;width:320px}
.kids .row h4{font-size:16px}
.kids .item{margin-bottom:10px}
/* desserts */
.desserts{left:395px;top:1388px;width:320px;height:314px;background:var(--red);color:var(--paper);padding:10px 16px}
.desserts h2{font-size:40px;margin-bottom:8px;display:flex;align-items:center;gap:12px}
.desserts .cake-art{width:58px;height:36px;background:linear-gradient(135deg,#f3c6bf,#e9a197)}
.desserts li{list-style:none;display:flex;justify-content:space-between;font-family:"Oswald",sans-serif;font-size:15px;text-transform:uppercase;line-height:23.5px}
.desserts li span{font-family:"Crimson Pro",serif;font-size:12px}
/* drinks */
.drinks-box{left:750px;top:1396px;width:322px;height:228px;border:1.5px dashed var(--red)}
.drinks-head{left:770px;top:1372px;background:var(--paper);padding:0 10px;font-size:40px}
.glass-art{left:935px;top:1344px;width:48px;height:80px}
.drinks{left:760px;top:1442px;width:302px}
.drinks li{list-style:none;display:flex;justify-content:space-between;font-family:"Oswald",sans-serif;font-size:15px;text-transform:uppercase;line-height:22px}
.drinks li span{font-family:"Crimson Pro",serif;font-size:12px;color:var(--red)}
.pizza-note{left:750px;top:1640px;width:325px;font-style:italic;font-weight:700;font-size:14.5px;line-height:18px}
</style>
</head>
<body>
<main class="menu">

  <header>
    <div class="abs brand"><span class="brand-dot"></span><span class="brand-name">Tolbert's</span></div>
    <p class="abs intro">Only the finest ingredients, the choicest cuts of meats and the freshest produce will be good enough for our customers. Our beef products are from the round cut (leanest possible) therefore the most <b>“heart healthy”</b>. Our turkey is smoked breast 98% fat free. We make our salads fresh from scratch. We want you to know these facts so you will understand why we feel we are unique in the Permian Basin. To state our philosophy in a single word, it is <b>“QUALITY”</b>.</p>
    <div class="abs contact">
      <span><svg viewBox="0 0 12 16"><path d="M6 0a6 6 0 0 0-6 6c0 4.5 6 10 6 10s6-5.5 6-10a6 6 0 0 0-6-6zm0 8.5A2.5 2.5 0 1 1 6 3.5a2.5 2.5 0 0 1 0 5z" fill="#d9493a"/></svg>418 E. Lanham Ave, Crestvale, Texas 79512</span>
      <span><svg viewBox="0 0 16 16"><path d="M3.5 1l3 3-1.8 2a9 9 0 0 0 5.3 5.3l2-1.8 3 3-2 2.5C6.5 14.5 1.5 9.5.9 3z" fill="#d9493a"/></svg>(432) 555-0186</span>
      <span><svg viewBox="0 0 16 16"><circle cx="8" cy="8" r="7" fill="none" stroke="#d9493a" stroke-width="1.6"/><path d="M1 8h14M8 1c-3 4-3 10 0 14M8 1c3 4 3 10 0 14" fill="none" stroke="#d9493a" stroke-width="1.3"/></svg>www.tolbertsonlanham.com</span>
    </div>
    <div class="abs rule"></div>
  </header>

  <!-- Soup & Salad -->
  <h2 class="abs sec soup-head">Soup <span class="amp">&amp;</span><br>Salad</h2>
  <div class="abs art soup-art" role="img" aria-label="Line drawing of a steaming soup bowl"></div>
  <section class="abs soup-list">
    <div class="soup">Cream of Broccoli Potato with Bacon</div>
    <div class="soup">Chicken Noodle</div>
    <div class="soup">Wisconsin Cheese</div>
    <div class="soup">Tomato Basil &nbsp;| &nbsp;<span class="price">Cup $ 4.25 Bowl $ 5.25</span></div>
    <div class="soup">Seafood Gumbo &nbsp;| &nbsp;<span class="price">Cup $ 5.50 &nbsp;Bowl $ 6.50</span></div>
  </section>
  <section class="abs salads">
    <div class="item"><div class="row"><h4>Chicken Salad Plate</h4><span class="price">$ 9.95</span></div><p>Chicken salad served on tomato wedge or avocado half, with Swiss and cheddar cheese and a side order of your choice.</p></div>
    <div class="item"><div class="row"><h4>Tuna or Krab Salad Plate</h4><span class="price">$ 10.75</span></div><p>Tuna or Krab salad served on tomato wedge or avocado half, with Swiss and cheddar cheese and a side order of your choice.</p></div>
    <div class="item"><div class="row"><h4>Fit “Chick”en</h4><span class="price">$ 13.09</span></div><p>Grilled or Blackened Chicken served on a bed of spinach with half an avocado and Tolbert's steam grilled veggies with your choice of salad dressing</p></div>
    <div class="item"><div class="row"><h4>Tuna or Krab Salad Plate</h4><span class="price">$ 10.75</span></div><p>Tuna or Krab salad served on tomato wedge or avocado half, with Swiss and cheddar cheese and a side order of your choice.</p><div class="add"><span>&nbsp;With grilled or blackened salmon, shrimp or Tuna</span><span class="price">$ 15.05</span></div></div>
    <div class="item"><div class="row"><h4>Caesar Salad</h4><span class="price">$ 6.09</span></div><div class="add"><span>Add grilled or blackened chicken breast</span><span class="price">$ 8.09</span></div><div class="add"><span>Add grilled or blackened tuna, salmon or shrimp</span><span class="price">$ 10.09</span></div></div>
    <div class="item"><div class="row"><h4>Heavenly Salad</h4><span class="price">$ 11.05</span></div><p>Romaine lettuce, bacon bits, grilled chicken, mandarin oranges, toasted almonds with poppy seed dressing.</p></div>
    <div class="item"><div class="row"><h4>Super Spinach Salad</h4><span class="price">$ 13.09</span></div><p>Baby spinach, eggs, purple onions, bacon bits, roasted red peppers and bleu cheese crumbles.</p><div class="add"><span>With grilled or blackened chicken</span><span class="price">$ 13.05</span></div><div class="add"><span>With grilled or blackened tuna, salmon or shrimp</span><span class="price">$ 15.05</span></div></div>
    <div class="item"><div class="row"><h4>Turkey Bowl</h4><span class="price">$ 11.05</span></div><p>A Caesar salad topped with pasta salad, cubed turkey breast and fresh grated parmesan</p></div>
    <div class="item"><div class="row"><h4>Chef Salad</h4><span class="price">$ 11.05</span></div><p>Lettuce, tomato, turkey, ham, shredded cheese, sliced eggs</p></div>
    <div class="item"><div class="row"><h4>Arugula Salad</h4><span class="price">$ 11.25</span></div><p>Arugula, candied walnuts, thinly sliced green apples, dried cranberries, bleu cheese, lemon herb vinaigrette</p><div class="add"><span>With grilled or blackened chicken breast</span><span class="price">$ 13.25</span></div><div class="add"><span>With blackened salmon, tuna, or shrimp</span><span class="price">$ 15.05</span></div></div>
  </section>

  <!-- Cold Sandwiches -->
  <h2 class="abs sec cold-band">Cold Sandwiches</h2>
  <section class="abs cold">
    <p class="note sides">Choose one of the following sides:<br>Potato Salad * Cole Slaw * Potato Chips * Pasta Salad * Ranch Style Beans * Mixed Fruit Cup * Curly “Q” Fries</p>
    <p class="extras">Extra side order <span class="red">$ 2.25</span> • Grilled veggies <span class="red">$ 3</span><br>Sweet potato curly fries <span class="red">$ 4</span><br>Roast beef - corned beef -ham <span class="red">$ 6.75</span><br>Turkey - pastrami - salami</p>
    <div class="item"><div class="row"><h4>B*LT</h4><span class="price">$ 8.50</span></div><p>A standard BLT with extra bacon</p></div>
    <div class="item"><div class="row"><h4>Club Sandwich</h4><span class="price">$ 10.09</span></div><p>The traditional favorite (ham, turkey and bacon triple decker) enhanced by Tolbert's quality and quantity</p></div>
    <div class="item"><div class="row"><h4>California Club</h4><span class="price">$ 10.09</span></div><p>Ham, turkey, avocado, sprouts, tomato and black olives on a croissant</p></div>
    <div class="item"><div class="row"><h4>Turk-Ado</h4><span class="price">$ 10.09</span></div><p>Triple decker sandwich with turkey, avocado, bacon &amp; sprouts</p></div>
    <div class="item"><div class="row"><h4>Chicken Salad Sandwich</h4><span class="price">$ 7.75</span></div></div>
    <div class="item"><div class="row"><h4>Tuna or Krab Salad Sandwich</h4><span class="price">$ 8.75</span></div></div>
  </section>

  <!-- Hot Sandwiches -->
  <div class="abs hot-head"><div class="bar"></div><h2 class="sec">Hot Sandwiches</h2><div class="bar"></div></div>
  <section class="abs hot-a">
    <div class="item"><div class="row"><h4>Grilled Cheese Sandwich</h4><span class="price">$ 6.25</span></div><p>Grilled with your choice of: Swiss, provolone, American, cheddar or pepper jack</p></div>
    <div class="item"><div class="row"><h4>Beer Brats</h4><span class="price">$ 6.50</span></div><p>Soaked in beer with grilled onions and sauerkraut on a toasted French roll</p></div>
    <div class="item"><div class="row"><h4>Beefeater</h4><span class="price">$ 9.35</span></div><p>Thin sliced roast beef on white bread with horseradish sauce, melted Swiss and tomato slices</p></div>
    <div class="item"><div class="row"><h4>French Dip</h4><span class="price">$ 9.05</span></div><p>Lean roast beef served on a steak bun with melted provolone, au jus... cest magnifique!<br>Try it with Chicago-Style Giardiniera + 1</p></div>
    <div class="item"><div class="row"><h4>Philly</h4><span class="price">$ 10.35</span></div><p>Lean roast beef with grilled onions and cheddar cheese on a fresh baked French roll</p></div>
    <div class="item"><div class="row"><h4>Reuben</h4><span class="price">$ 10.05</span></div><p>Lean corned beef on grilled rye with melted Swiss, Reuben dressing and sauerkraut ..mmm good!</p></div>
    <div class="item"><div class="row"><h4>Rachel (Turkey Reuben)</h4><span class="price">$ 10.05</span></div><p>Turkey on grilled rye with melted Swiss, Reuben dressing and sauerkraut</p></div>
  </section>
  <section class="abs hot-b">
    <div class="item"><div class="row"><h4>Hot Pastrami</h4><span class="price">$ 9.35</span></div><p>Served with Swiss on rye</p></div>
    <div class="item"><div class="row"><h4>Krabmelt</h4><span class="price">$ 10.35</span></div><p>Fresh krab salad, melted Swiss served on grilled rye bread</p></div>
    <div class="item"><div class="row"><h4>Grilled Chicken Sandwich</h4><span class="price">$ 9.75</span></div><p>Strips of grilled chicken breast served on a toasted bun with lettuce and tomato</p></div>
    <div class="item"><div class="row"><h4>Blackened Chicken Sandwich</h4><span class="price">$ 9.75</span></div><p>Strips of blackened chicken breast served on a whole wheat bun with lettuce and tomato</p></div>
    <div class="item"><div class="row"><h4>Chik-Ado</h4><span class="price">$ 10.15</span></div><p>Strips of marinated chicken on a wheat bun topped with bacon, pepper jack cheese, sprouts and avocado.</p></div>
    <div class="item"><div class="row"><h4>Chicken Fried Steak Sandwich</h4><span class="price">$ 10.05</span></div><p>With lettuce and tomato on a toasted bun</p></div>
    <div class="item"><div class="row"><h4>Veggie Pita</h4><span class="price">$ 9.05</span></div><p>Fresh garden veggies sautéed with olive oil, seasoned &amp; served in a pita pocket</p><div class="add"><span>With grilled or blackened chicken breast</span><span class="price">$ 11.09</span></div><div class="add"><span>With grilled our blackened shrimp</span><span class="price">$ 14.09</span></div><div class="add"><span>Add <span class="red">4 Oz.</span> hummus <span class="red">$ 2.25</span> OR <span class="red">4 oz.</span> tzatziki <span class="red">$ 1.25</span></span></div></div>
  </section>

  <!-- Burgers & Dog -->
  <svg class="abs burger-band" width="642" height="86" viewBox="0 0 642 86" aria-hidden="true">
    <path d="M20 1H622L641 20V66L622 85H20L1 66V20Z" fill="none" stroke="#161616" stroke-width="1.5"/>
    <path d="M26 8H616L632 24V62L616 78H26L10 62V24Z" fill="#d9493a"/>
    <line x1="30" y1="43" x2="88" y2="43" stroke="#fbf8ef" stroke-width="2.5"/>
    <line x1="560" y1="43" x2="612" y2="43" stroke="#fbf8ef" stroke-width="2.5"/>
  </svg>
  <div class="abs art burger-art" role="img" aria-label="Drawn burger illustration"></div>
  <h2 class="abs sec burger-title">Burgers &amp; Dog</h2>
  <div class="abs art dog-art" role="img" aria-label="Drawn hot dog illustration"></div>
  <p class="abs burger-opts">Try it on ajalapeño bun! <span class="red">$ 1.20</span> &nbsp;•&nbsp; add fried egg <span class="red">$ 1</span> &nbsp;•&nbsp; add cheese <span class="red">$ 1</span></p>
  <section class="abs burger-a">
    <div class="item"><div class="row"><h4>Tolbert's Best Burger</h4><span class="price">$ 7.09</span></div><p>100% ground beef on a toasted bun</p></div>
    <div class="item"><div class="row"><h4>Super Burger</h4><span class="price">$ 10.39</span></div><p>Our “Best Burger” enhanced with bacon, avocado, Swiss and cheddar cheese, sprouts, served on a toasted bun</p></div>
    <div class="item"><div class="row"><h4>Tolbert Melt</h4><span class="price">$ 8.65</span></div><p>100% ground beef with Swiss cheese, served on rye bread</p></div>
    <div class="item"><div class="row"><h4>Jalapeño Burger</h4><span class="price">$ 10.45</span></div><p>100% ground beef with pepper jack cheese, bacon and served on a jalapeño bun</p><div class="add" style="line-height:14px"><span>100% ground beef with green chile peppers, Swiss cheese on a toasted bun</span><span class="price">$ 9.95</span></div></div>
    <div class="item"><div class="row"><h4>Bacon Jam Arugula Burger</h4><span class="price">$ 10.99</span></div><p>100% ground beef with bacon jam, white cheddar, arugula and a drizzle of balsamic reduction on a toasted bun</p></div>
  </section>
  <section class="abs burger-b">
    <div class="item"><div class="row"><h4>Hot Dog</h4><span class="price">$ 6.25</span></div><p>All beef frank</p></div>
    <div class="item"><div class="row"><h4>Chicago Dog</h4><span class="price">$ 6.50</span></div><p>All beef frank with hot giardiniera relish</p></div>
    <div class="item"><div class="row"><h4>Chili Dog</h4><span class="price">$ 6.99</span></div><p>All beef frank with chili, cheese, and onions</p></div>
    <div class="item"><div class="row"><h4>The Works Dog</h4><span class="price">$ 7.25</span></div><p>All beef frank with chili, cheese, and onions and giardimiera relish</p></div>
    <div class="item"><div class="row"><h4>Mac &amp; Cheese Dog</h4><span class="price">$ 7.75</span></div><p>All beef frank with mac &amp; cheese and green onion</p></div>
  </section>

  <!-- Appetizers -->
  <div class="abs app-head">
    <svg viewBox="0 0 22 20" aria-hidden="true"><path d="M2 10H20M6 4L2 10L6 16M12 4L8 10L12 16" fill="none" stroke="#d9493a" stroke-width="1.8"/></svg>
    <h2 class="sec">Appetizers</h2>
    <svg viewBox="0 0 22 20" aria-hidden="true"><path d="M2 10H20M16 4L20 10L16 16M10 4L14 10L10 16" fill="none" stroke="#d9493a" stroke-width="1.8"/></svg>
  </div>
  <section class="abs app">
    <div class="item"><div class="row"><h4>Breaded Cheese Sticks</h4><span class="price">$ 10.50</span></div><p>“Signature” marinara sauce <span class="red">$ +1.25</span></p></div>
    <div class="item"><div class="row"><h4>Zucchini Chips</h4><span class="price">$ 9.95</span></div><p>“Signature” marinara sauce <span class="red">$ +1.25</span></p><div class="add" style="line-height:14px;margin-top:4px"><span>Onion Rings</span><span class="price">$ 9.95</span></div><div class="add" style="line-height:14px"><span>Chips &amp; Queso</span><span class="price">$ 6.25</span></div></div>
    <div class="item"><div class="row"><h4>Potachos</h4><span class="price">$ 10.05</span></div><p>with blackened or grilled chicken <span class="red">$ 12.25</span></p></div>
  </section>

  <!-- Desserts -->
  <section class="abs desserts">
    <h2 class="sec">Desserts <span class="art cake-art" role="img" aria-label="Drawn slice of cake"></span></h2>
    <ul>
      <li>Iced Brownies<span>$ 2.15</span></li>
      <li>Carrot Cake<span>$ 4.00</span></li>
      <li>Boston Cream Pie<span>$ 4.00</span></li>
      <li>Key Lime Pie<span>$ 6.25</span></li>
      <li>Chocolate Mousse Cake<span>$ 6.50</span></li>
      <li>New York Colossal Cheesecake<span>$ 6.25</span></li>
      <li>‘The “Real Deal” Cannoli<span>$ 6.50</span></li>
      <li>Lemon Tart<span>$ 3.25</span></li>
      <li>‘Texas Chocolate Sheet Cake<span>$ 4.50</span></li>
      <li>Italian Cream Cake<span>$ 4.50</span></li>
    </ul>
  </section>

  <!-- Kids Menu -->
  <svg class="abs kids-band" width="300" height="90" viewBox="0 0 300 90" aria-hidden="true">
    <path d="M0 30H40V80H22L26 62Z" fill="#a8322a"/>
    <path d="M300 30H260V80H278L274 62Z" fill="#a8322a"/>
    <path d="M28 20L40 80V30Z" fill="#7a231d"/>
    <path d="M272 20L260 80V30Z" fill="#7a231d"/>
    <rect x="28" y="0" width="244" height="66" fill="#d9493a"/>
  </svg>
  <h2 class="abs sec kids-title">★ Kids Menu ★</h2>
  <section class="abs kids">
    <div class="item"><div class="row"><h4>Mac and Cheese</h4><span class="price" style="text-align:right;line-height:13px">Cup $ 3.00<br>Bowl $ 4.50</span></div></div>
    <div class="item"><div class="row"><h4>All Beef Hot Dog</h4><span class="price">$ 6.25</span></div></div>
    <div class="item"><div class="row"><h4>Peanut Butter &amp; Jelly with Side</h4><span class="price">$ 6.00</span></div></div>
    <div class="item"><div class="row"><h4>Grilled Cheese Sandwich with Side</h4><span class="price">$ 6.25</span></div></div>
    <div class="item"><div class="row"><h4>Apple Juice</h4><span class="price">$ 1.50</span></div></div>
  </section>

  <!-- Drinks -->
  <div class="abs drinks-box"></div>
  <h2 class="abs sec drinks-head">Drinks</h2>
  <div class="abs art glass-art" role="img" aria-label="Drawn glass with ice and straw"></div>
  <ul class="abs drinks">
    <li>Cola, Diet Cola, Cherry Cola,</li>
    <li>Lemon-Lime, Root Beer, Pepper Soda, Cream</li>
    <li>Soda, Tea, Raspberry Tea, Lemonade,</li>
    <li>Coffee (Regular or Decaf),</li>
    <li>Sparkling Mineral Water<span>$ 2.49</span></li>
    <li>Bottled Water<span>$ 1.95</span></li>
    <li>Electrolyte Water<span>$ 3.45</span></li>
    <li>Large Drinks<span>$ 3.39</span></li>
  </ul>
  <p class="abs pizza-note">Tolbert's Homemade Wood-Fire Brick Oven Frozen Pizza Available for Purchase Any Time or Day of the Week!</p>

</main>
</body>
</html>
```